New Managed IT company needs a business card

We are an IT management and support company that needs a business card design. I have a logo that I'll provide. Blues and blacks match the logo, but i'm open to anything. I want the card to help people take us seriously, but still have some energy and fun in it. The card should communicate stability and a solid company.

Target Market(s)

Target market includes Owners and Presidents at small businesses of 20 - 100 employees in the Pittsburgh PA area.

Industry/Entity Type

Information Technology

Contact Information for Business Card

i am open to other designs, but i imagine having only the logo on one side and then the logo plus all contact details on the other side.

Requirements
Must have
• Our logo
• Company name is optional if the logo makes it obvious
• A name - Cole Perrin
• A title - President
• A phone number - 724-XXX-XXXX
• A mobile phone number - 724-615-2748
• An email address - cperrin@techvaultgrid.com
• a website - techvaultgrid.com or www.techvaultgrid.com
Nice to have
• some people tell me the logo feels like a superhero theme, some fun with that idea might be good. I'm open to ideas.
Should not have
• stock photos of people or computers - especially old looking stuff.

```html
<!DOCTYPE html>
<html lang="en">
<head>
<meta charset="UTF-8">
<title>TechVault Grid – Business Card</title>
<link href="https://fonts.googleapis.com/css2?family=Lato:wght@400;700;900&display=swap" rel="stylesheet">
<style>
  :root {
    --page-bg: #e6e8eb;
    --brand-blue: #0a6fd1;
    --brand-blue-light: #1aa3ec;
    --brand-blue-deep: #1d47b5;
    --ink: #1c1d20;
    --charcoal: #3a3d42;
    --white: #ffffff;
    --name-blue: #0b6cc4;
  }
  * { box-sizing: border-box; margin: 0; padding: 0; }
  html, body {
    width: 1200px;
    height: 900px;
    overflow: hidden;
    background: var(--page-bg);
    font-family: "Lato", sans-serif;
  }
  .canvas {
    position: relative;
    width: 1200px;
    height: 900px;
  }
  .card {
    position: absolute;
    left: 320px;
    width: 560px;
    height: 320px;
    overflow: hidden;
    box-shadow: 0 10px 28px rgba(0,0,0,0.22);
  }

  /* Back side */
  .card--back {
    top: 90px;
    background: radial-gradient(ellipse at 45% 55%, var(--brand-blue-light) 0%, var(--brand-blue) 50%, var(--brand-blue-deep) 100%);
    color: var(--white);
  }
  .back-brand {
    position: absolute;
    top: 92px;
    left: 0;
    width: 100%;
    display: flex;
    flex-direction: column;
    align-items: center;
    gap: 16px;
  }
  .brand-dot {
    width: 74px;
    height: 74px;
    border-radius: 50%;
    background: var(--white);
  }
  .back-brand .brand-name {
    font-size: 38px;
    font-weight: 900;
    letter-spacing: 3px;
    text-transform: uppercase;
    color: var(--white);
  }
  .back-web {
    position: absolute;
    bottom: 40px;
    width: 100%;
    text-align: center;
    font-size: 15px;
    letter-spacing: 1.5px;
  }

  /* Front side */
  .card--front {
    top: 490px;
    background: var(--white);
  }
  .front-brand {
    position: absolute;
    top: 30px;
    left: 34px;
    display: flex;
    align-items: center;
    gap: 12px;
  }
  .front-brand .brand-dot {
    width: 46px;
    height: 46px;
    background: var(--ink);
  }
  .front-brand .brand-name {
    font-size: 24px;
    font-weight: 900;
    letter-spacing: 2px;
    text-transform: uppercase;
    color: var(--ink);
  }
  .contact-list {
    position: absolute;
    top: 112px;
    left: 36px;
    list-style: none;
    font-size: 14px;
    color: var(--ink);
    line-height: 24px;
  }
  .contact-list li {
    display: flex;
    align-items: center;
    gap: 10px;
  }
  .contact-list svg {
    width: 13px;
    height: 13px;
    fill: var(--name-blue);
    flex: none;
  }
  .person {
    position: absolute;
    top: 150px;
    right: 44px;
    text-align: right;
  }
  .person-name {
    font-size: 27px;
    color: var(--name-blue);
    font-weight: 400;
  }
  .person-title {
    font-size: 16px;
    color: var(--ink);
    margin-top: 2px;
  }
  .front-swoosh {
    position: absolute;
    left: 0;
    bottom: 0;
    width: 560px;
    height: 320px;
  }
  .front-web {
    position: absolute;
    bottom: 13px;
    left: 120px;
    font-size: 15px;
    letter-spacing: 1.2px;
    color: var(--white);
  }
</style>
</head>
<body>
<main class="canvas">

  <section class="card card--back" aria-label="Card back">
    <div class="back-brand">
      <span class="brand-dot"></span>
      <span class="brand-name">TechVault Grid</span>
    </div>
    <p class="back-web">www.techvaultgrid.com</p>
  </section>

  <section class="card card--front" aria-label="Card front">
    <svg class="front-swoosh" viewBox="0 0 560 320" aria-hidden="true">
      <defs>
        <linearGradient id="bandBlue" x1="0" y1="0" x2="1" y2="0">
          <stop offset="0" stop-color="#1b95e0"/>
          <stop offset="1" stop-color="#1d47b5"/>
        </linearGradient>
      </defs>
      <path d="M0 232 C170 262 320 300 560 262 L560 320 L0 320 Z" fill="url(#bandBlue)"/>
      <path d="M0 226 C170 268 340 272 560 240 L560 258 C340 292 170 282 0 238 Z" fill="#3a3d42"/>
      <path d="M0 238 C170 282 340 292 560 258 L560 266 C340 300 170 290 0 246 Z" fill="#ffffff"/>
    </svg>

    <div class="front-brand">
      <span class="brand-dot"></span>
      <span class="brand-name">TechVault Grid</span>
    </div>

    <ul class="contact-list">
      <li>
        <svg viewBox="0 0 24 24"><path d="M6.6 10.8a15.5 15.5 0 0 0 6.6 6.6l2.2-2.2c.3-.3.7-.4 1-.2 1.1.4 2.3.6 3.6.6.6 0 1 .4 1 1V20c0 .6-.4 1-1 1C10.6 21 3 13.4 3 4c0-.6.4-1 1-1h3.5c.6 0 1 .4 1 1 0 1.3.2 2.5.6 3.6.1.3 0 .7-.2 1z"/></svg>
        <span>724-615-2700</span>
      </li>
      <li>
        <svg viewBox="0 0 24 24"><path d="M7 1h10a2 2 0 0 1 2 2v18a2 2 0 0 1-2 2H7a2 2 0 0 1-2-2V3a2 2 0 0 1 2-2zm0 3v14h10V4zm5 15.5a1 1 0 1 0 0 2 1 1 0 0 0 0-2z"/></svg>
        <span>724-615-2748</span>
      </li>
      <li>
        <svg viewBox="0 0 24 24"><path d="M2 5h20v14H2zm2 2v.5l8 5.5 8-5.5V7zm0 3v7h16v-7l-8 5.5z"/></svg>
        <span>cperrin@techvaultgrid.com</span>
      </li>
    </ul>

    <div class="person">
      <p class="person-name">Cole Perrin</p>
      <p class="person-title">President</p>
    </div>

    <p class="front-web">www.techvaultgrid.com</p>
  </section>

</main>
</body>
</html>
```